Zielgruppe
Ich erstelle und vermarkte hochwertige Ebooks/Taschenbücher über Veltrano. Zielgruppe sind Veltrano Lumio Kunden.
Translate to english with google translater:
I create and market high-quality ebooks/paperbacks via Veltrano. The target group are Veltrano Lumio customers.
Aufgabenstellung
Es geht sowohl um die Gestaltung eines Taschenbuch-Covers als auch um die Gestaltung eines Ebook-Covers.
Die Gesamtaufmachung soll schlicht und in sich stimmig sein, ohne viel Schnörkel.
Der Buchtitel lautet wie folgt: Kochbuch für Hobbyköche, Anfänger, Berufstätige und Studenten
Der Untertitel in etwa halber Schriftgröße lautet wie folgt: Mit den 150 besten und originellsten Rezepten für einen perfekten Einstieg
Pseudonym des Autors am unteren Ende: Matthias Wendrauer
Farbliche Aufmachung: Der Hintergrund ein sehr dunkles Rot, Außen ganz dunkel, nach Innen hin zur Mitte etwas heller in fließendem Übergang. Die Schrift in schlichtem Weiß.
Gestalterische Aufmachung: Normale Schriftart. Ausgenommen 'Kochbuch', 'Kochbuch' in Schriftart ähnlich wie Schriftart Monotype Corsiva. Im unterem Bereich Rechts ein Bild eines bunten originellen Gerichts - Nudelgericht - aus der Vogelperspektive, Links einige Gewürze verstreut und einen echten Kochlöffel in dunklem Braun. Genaue Anordnung überlasse ich dem Designer.
It's about designing a paperback cover as well as designing an ebook cover.
The overall presentation should be simple and coherent, without a lot of frills.
The book title is as follows: Kochbuch für Hobbyköche, Anfänger, Berufstätige und Studenten
The subtitle in about half font size is as follows: Mit den 150 besten und originellsten Rezepten für einen perfekten Einstieg
Author's pseudonym at the bottom: Matthias Wendrauer
Color presentation: The background is a very dark red, very dark on the outside, slightly lighter towards the middle in a flowing transition. The font is plain white.
Design: Normal font. Except 'Kochbuch', 'Kochbuch' in font similar to Monotype Corsiva font. In the lower area on the right a picture of a colorful original dish - pasta dish - from a bird's eye view, on the left some spices scattered around and a real wooden spoon in dar..

```html
<!DOCTYPE html>
<html lang="de">
<head>
<meta charset="utf-8">
<title>Kochbuch – Cover</title>
<link rel="stylesheet" href="https://fonts.googleapis.com/css2?family=Alegreya:ital,wght@1,700&family=Raleway:wght@400;500&display=swap">
<style>
  :root {
    --bg-centre: #741a2c;
    --bg-mid: #5e1323;
    --bg-edge: #420b17;
    --text-white: #ffffff;
    --spoon-light: #b8744a;
    --spoon-dark: #7a3e22;
    --plate-rim: #1c2230;
    --plate-blue: #1f3f7a;
    --pasta-yellow: #e6cf7c;
    --pasta-green: #7fa44a;
    --spice-green: #4f6a3a;
    --spice-wood: #9a6a3c;
  }
  html, body {
    margin: 0;
    padding: 0;
    width: 750px;
    height: 1200px;
    overflow: hidden;
    background: var(--bg-edge);
  }
  .cover {
    position: relative;
    width: 750px;
    height: 1200px;
    overflow: hidden;
    background: radial-gradient(ellipse 70% 60% at 50% 48%, var(--bg-centre) 0%, var(--bg-mid) 55%, var(--bg-edge) 100%);
  }
  .spoon-photo {
    position: absolute;
    left: -60px;
    top: 70px;
    width: 560px;
    height: 270px;
    border-radius: 50% 48% 48% 50% / 55% 50% 50% 55%;
    transform: rotate(6deg);
    background: radial-gradient(ellipse 45% 60% at 70% 50%, var(--spoon-light) 0%, var(--spoon-dark) 100%);
  }
  .title-script {
    position: absolute;
    left: 0;
    top: 0;
    width: 750px;
    height: 360px;
    margin: 0;
    font-family: "Alegreya", "Times New Roman", serif;
    font-style: italic;
    font-weight: 700;
    color: var(--text-white);
    font-size: 150px;
    line-height: 1;
  }
  .title-script .word {
    position: absolute;
    display: block;
    transform: rotate(-6deg);
    transform-origin: left bottom;
  }
  .title-script .word-koch { left: 114px; top: 92px; }
  .title-script .word-buch { left: 218px; top: 200px; }
  .title-main {
    position: absolute;
    top: 400px;
    left: 0;
    width: 750px;
    margin: 0;
    text-align: center;
    font-family: "Raleway", Arial, sans-serif;
    font-weight: 500;
    font-size: 41px;
    line-height: 54px;
    color: var(--text-white);
  }
  .subtitle {
    position: absolute;
    top: 530px;
    left: 0;
    width: 750px;
    margin: 0;
    text-align: center;
    font-family: "Raleway", Arial, sans-serif;
    font-weight: 400;
    font-size: 23.5px;
    line-height: 37px;
    color: var(--text-white);
  }
  .spices-photo {
    position: absolute;
    left: -40px;
    top: 760px;
    width: 320px;
    height: 350px;
    border-radius: 45% 55% 50% 45% / 40% 45% 55% 60%;
    background: radial-gradient(ellipse 60% 55% at 45% 50%, var(--spice-green) 0%, var(--spice-wood) 55%, rgba(94, 19, 35, 0) 100%);
  }
  .dish-photo {
    position: absolute;
    left: 440px;
    top: 618px;
    width: 668px;
    height: 668px;
    border-radius: 50%;
    background: radial-gradient(circle at 50% 50%, var(--pasta-yellow) 0%, var(--pasta-green) 38%, var(--plate-blue) 58%, var(--plate-rim) 68%);
  }
  .author {
    position: absolute;
    top: 1120px;
    left: 0;
    width: 720px;
    margin: 0;
    text-align: center;
    font-family: "Raleway", Arial, sans-serif;
    font-weight: 500;
    font-size: 18px;
    letter-spacing: 4.5px;
    text-transform: uppercase;
    color: var(--text-white);
  }
</style>
</head>
<body>
<main class="cover">
  <div class="spoon-photo" role="img" aria-label="Kochlöffel aus dunklem Holz von oben"></div>
  <div class="spices-photo" role="img" aria-label="Verstreute Gewürze: Knoblauch, Rosmarin, Meersalz und bunter Pfeffer in Holzschälchen"></div>
  <div class="dish-photo" role="img" aria-label="Bandnudeln mit grünem Spargel, Pistazien, Parmesan und Basilikum auf blauem Teller, von oben"></div>

  <h1 class="title-script">
    <span class="word word-koch">Koch</span>
    <span class="word word-buch">buch</span>
  </h1>

  <p class="title-main">Für Hobbyköche, Anfänger,<br>Berufstätige und Studenten</p>

  <p class="subtitle">Mit den 150 besten und originellsten Rezepten<br>für einen perfekten Einstieg</p>

  <p class="author">Matthias Wendrauer</p>
</main>
</body>
</html>
```